Hackthon event need a Landing Page

We are looking for a landing page to represent an event we are preparing in our country (Dominican Republic), it would be the first of this type, and we want to create a positive impact and make it a brand to make it recurring year to year .

The event is a hackathon where we will be gathering students and professionals to solve challenges using software development.

This landing page should be resposive, multi-language, clean, modern and align with the event logo.

Find a good example of what we are looking for in the following link:

https://brightcodefest.example/

We would like to have the following sections(Not necesarily in this order, not necesarily all of them):

- Brief
- Agenda
- Countdown
- Form Button to redirect to the event registration service.
---> Note: We would like to see the option of having the form in the landing page.
- Contact info and Social Media
- Partners/Sponsors
- Link to intro video

We will be attaching the logo and the variations of colors we are looking to see. It should be with a black background

```html
<!DOCTYPE html>
<html lang="en">
<head>
<meta charset="utf-8">
<title>ByteQuest Hackathon</title>
<link href="https://fonts.googleapis.com/css2?family=Rye&family=Orbitron:wght@500&family=Roboto:wght@400;500;700&display=swap" rel="stylesheet">
<style>
:root{
  --bg:#0a0a0a;
  --header:#000;
  --panel:#000;
  --card:#050505;
  --footer:#111;
  --accent:#f5776a;
  --accent-soft:#f78a7c;
  --link:#3fc5c5;
  --text:#fff;
  --muted:#d8d8d8;
  --line:#2a2a2a;
}
*{box-sizing:border-box;margin:0;padding:0}
html,body{width:1200px;height:2525px;overflow:hidden}
body{background:var(--bg);color:var(--text);font-family:'Roboto',sans-serif;position:relative}
.abs{position:absolute}
/* header */
.site-header{left:0;top:0;width:1200px;height:97px;background:var(--header)}
.brand-badge{left:112px;top:-30px;width:160px;height:158px;border-radius:50%;background:var(--header);display:flex;align-items:flex-end;justify-content:center;padding-bottom:38px;z-index:3}
.brand-badge span{font-family:'Roboto',sans-serif;font-weight:700;font-size:20px;color:var(--accent)}
.nav a{position:absolute;top:37px;font-size:15px;color:var(--text);text-decoration:none}
.nav a.active{color:var(--accent-soft)}
.nav a.active::after{content:"";position:absolute;left:0;right:0;top:25px;height:1px;background:var(--accent)}
.lang{left:828px;top:33px;display:flex;align-items:center;gap:10px;font-weight:700;font-size:15px}
.lang i{display:block;width:27px;height:27px;border-radius:50%;background:#2b3f86;border:3px solid #e0e0e0}
.btn{background:var(--accent);color:#fff;font-weight:500;font-size:15px;display:flex;align-items:center;justify-content:center;gap:10px;border-radius:2px}
.register{left:939px;top:23px;width:147px;height:46px}
/* hero */
.hero{left:0;top:97px;width:1200px;height:711px;background:linear-gradient(100deg,#3a3a40 0%,#4b4a4e 30%,#2d2a2c 55%,#5a3a34 75%,#3a2c28 100%)}
.hero-title{left:0;top:410px;width:1200px;text-align:center;font-family:'Rye',serif;font-size:50px;letter-spacing:1px;text-shadow:0 2px 6px #000}
.count{top:528px;width:244px;text-align:center;text-shadow:0 2px 6px rgba(0,0,0,.6)}
.count b{display:block;font-family:'Orbitron',sans-serif;font-weight:500;font-size:58px;line-height:70px}
.count span{display:block;font-weight:700;font-size:25px;margin-top:6px}
.divider{top:520px;width:3px;height:141px;background:#fff}
/* about */
.about-media{left:0;top:926px;width:661px;height:509px;background:linear-gradient(120deg,#c9c9c6 0%,#7b766f 40%,#3b3835 75%,#1d1b1a 100%)}
.play{left:287px;top:1157px;width:46px;height:46px}
.about-panel{left:531px;top:952px;width:610px;height:455px;background:var(--panel)}
.section-title{font-family:'Rye',serif;font-size:33px}
.about-title{left:598px;top:995px}
.about-text{left:598px;top:1053px;width:478px;font-size:15.2px;line-height:25.7px;text-align:justify;color:var(--muted)}
.learn{left:598px;top:1308px;width:164px;height:47px}
/* agenda */
.agenda-title{left:0;top:1525px;width:1200px;text-align:center}
.agenda-card{top:1597px;width:311px;height:231px;background:var(--card);padding:24px 20px 24px 26px}
.agenda-card .num{font-size:25px;font-weight:700;color:var(--accent)}
.agenda-card h3{font-size:15px;font-weight:700;margin-top:18px}
.agenda-card p{font-size:15.4px;line-height:23px;color:var(--muted);margin-top:17px}
.agenda-card a{display:block;margin-top:10px;font-size:15px;font-weight:700;color:var(--link);text-decoration:none}
.arrow{top:1702px;width:20px;height:20px}
/* partners */
.partners-title{left:0;top:1912px;width:1200px;text-align:center}
.partner{top:1985px;width:176px;height:78px;border:1px solid #3a3a3a;display:flex;align-items:center;justify-content:center;gap:8px;font-size:26px;font-weight:500}
.partner i{width:24px;height:24px;border-radius:50%;background:var(--accent)}
/* footer */
.site-footer{left:0;top:2150px;width:1200px;height:375px;background:var(--footer)}
.footer-brand{left:112px;top:2245px;width:158px;height:158px;border-radius:50%;border:3px solid var(--accent);display:flex;align-items:center;justify-content:center;font-weight:700;font-size:24px;color:var(--accent)}
.f-head{top:2229px;font-size:15px;font-weight:700}
.f-links{left:375px;top:2270px;list-style:none;font-size:16px;line-height:31px}
.contact-item{left:565px;display:flex;align-items:flex-start;gap:12px;font-size:16px;line-height:22px}
.contact-item i{width:26px;height:26px;border-radius:50%;background:var(--accent);flex:none;display:flex;align-items:center;justify-content:center}
.newsletter-text{left:837px;top:2272px;width:260px;font-size:15px;line-height:21px}
.email-field{left:838px;top:2330px;width:251px;height:36px;border-radius:18px;background:#222;overflow:hidden;font-size:10px;color:#aaa;padding:12px 0 0 28px}
.email-send{right:0;top:0;width:48px;height:36px;background:var(--accent);display:flex;align-items:center;justify-content:center}
.social{top:2388px;width:30px;height:30px;border-radius:50%;background:#222}
.social.on{background:var(--accent)}
.chat{left:1123px;top:2427px;width:36px;height:36px;border-radius:50%;background:var(--link);display:flex;align-items:center;justify-content:center}
.footer-rule{left:112px;top:2455px;width:976px;height:1px;background:var(--line)}
.copyright{left:0;top:2480px;width:1200px;text-align:center;font-size:14px}
</style>
</head>
<body>

<header class="abs site-header">
  <div class="abs brand-badge"><span>ByteQuest</span></div>
  <nav class="nav">
    <a class="active" style="left:321px" href="#">HOME</a>
    <a style="left:399px" href="#">ABOUT</a>
    <a style="left:483px" href="#">AGENDA</a>
    <a style="left:562px" href="#">CHALLENGES</a>
    <a style="left:693px" href="#">CONTACT US</a>
  </nav>
  <div class="abs lang"><i></i>ENG
    <svg width="10" height="6" viewBox="0 0 10 6"><path d="M0 0h10L5 6z" fill="#fff"/></svg>
  </div>
  <div class="abs btn register">REGISTER</div>
</header>

<section class="abs hero" role="img" aria-label="Photo of developers working together at computers with code on screen"></section>
<h1 class="abs hero-title">WELCOME TO BYTEQUEST</h1>
<div class="abs count" style="left:105px"><b>02</b><span>Days</span></div>
<div class="abs divider" style="left:347px"></div>
<div class="abs count" style="left:349px"><b>05</b><span>Hours</span></div>
<div class="abs divider" style="left:591px"></div>
<div class="abs count" style="left:593px"><b>34</b><span>Minutes</span></div>
<div class="abs divider" style="left:835px"></div>
<div class="abs count" style="left:837px"><b>05</b><span>Seconds</span></div>

<div class="abs about-media" role="img" aria-label="Photo of a programmer typing on a laptop beside a code monitor"></div>
<svg class="abs play" viewBox="0 0 46 46"><circle cx="23" cy="23" r="23" fill="#fff"/><circle cx="23" cy="23" r="19" fill="#111"/><path d="M18 13l14 10-14 10z" fill="#fff"/></svg>
<div class="abs about-panel"></div>
<h2 class="abs section-title about-title">ABOUT US</h2>
<p class="abs about-text">Lorem ipsum dolor sit amet, consectetur adipiscing elit, sed do eiusmod tempor incididunt ut labore et dolore magna aliqua. Ut enim ad minim veniam, quis nostrud exercitation ullamco laboris nisi ut aliquip ex ea commodo consequat. Duis aute irure dolor in reprehenderit in voluptate velit esse cillum dolore eu fugiat nulla pariatur. Excepteur sint occaecat cupidatat non proident, sunt in culpa qui officia deserunt mollit anim id est laborumconsectetur adipiscing elit, sed do eiusmod tempor incididunt ut labore et dolore magna enim ad minim veniam, quis nostrud exercitation ullamco laboris nisied.</p>
<div class="abs btn learn">LEARN MORE
  <svg width="14" height="14" viewBox="0 0 14 14"><circle cx="7" cy="7" r="7" fill="#fff"/><path d="M4 7h5M7 4.5L9.5 7 7 9.5" stroke="#f5776a" stroke-width="1.8" fill="none"/></svg>
</div>

<h2 class="abs section-title agenda-title">AGENDA</h2>
<svg class="abs arrow" style="left:60px" viewBox="0 0 20 20"><path d="M13 4l-6 6 6 6" stroke="#fff" stroke-width="2" fill="none"/></svg>
<article class="abs agenda-card" style="left:110px">
  <div class="num">01</div><h3>LOREM IPSUM DOLOR SIT AMET</h3>
  <p>Lorem ipsum dolor sited consectetur adipiscing elit sed do eiusmod tempor incididunt sited consectetur</p>
  <a href="#">View More &nbsp;»</a>
</article>
<article class="abs agenda-card" style="left:443px">
  <div class="num">02</div><h3>LOREM IPSUM DOLOR SIT AMET</h3>
  <p>Lorem ipsum dolor sited consectetur adipiscing elit sed do eiusmod tempor incididunt sited consectetur</p>
  <a href="#">View More &nbsp;»</a>
</article>
<article class="abs agenda-card" style="left:776px">
  <div class="num">03</div><h3>LOREM IPSUM DOLOR SIT AMET</h3>
  <p>Lorem ipsum dolor sited consectetur adipiscing elit sed do eiusmod tempor incididunt sited consectetur</p>
  <a href="#">View More &nbsp;»</a>
</article>
<svg class="abs arrow" style="left:1120px" viewBox="0 0 20 20"><path d="M7 4l6 6-6 6" stroke="#fff" stroke-width="2" fill="none"/></svg>

<h2 class="abs section-title partners-title">PARTNERS/SPONSORS</h2>
<div class="abs partner" style="left:110px"><i></i>Nimbra</div>
<div class="abs partner" style="left:311px"><i></i>Orvio</div>
<div class="abs partner" style="left:512px"><i></i>Kestrel</div>
<div class="abs partner" style="left:713px"><i></i>Pinegate</div>
<div class="abs partner" style="left:914px"><i></i>Solvane</div>

<footer class="abs site-footer"></footer>
<div class="abs footer-brand">ByteQuest</div>
<h4 class="abs f-head" style="left:375px">QUICK LINKS</h4>
<ul class="abs f-links"><li>Home</li><li>About Us</li><li>Agenda</li><li>Challenges</li><li>Contact Us</li></ul>
<h4 class="abs f-head" style="left:565px">CONTACT US</h4>
<div class="abs contact-item" style="top:2270px"><i><svg width="12" height="12" viewBox="0 0 12 12"><path d="M2 1l2.5 0 1 3-1.5 1a7 7 0 0 0 3 3l1-1.5 3 1V10a1 1 0 0 1-1 1A10 10 0 0 1 1 2a1 1 0 0 1 1-1z" fill="#fff"/></svg></i><span style="padding-top:2px">+1 555 014 2290</span></div>
<div class="abs contact-item" style="top:2321px"><i><svg width="12" height="10" viewBox="0 0 12 10"><rect width="12" height="10" rx="1" fill="#fff"/><path d="M0 1l6 4 6-4" stroke="#f5776a" fill="none"/></svg></i><span style="padding-top:2px">info@bytequest.example</span></div>
<div class="abs contact-item" style="top:2360px"><i><svg width="10" height="13" viewBox="0 0 10 13"><path d="M5 0a5 5 0 0 1 5 5c0 3-5 8-5 8S0 8 0 5a5 5 0 0 1 5-5z" fill="#fff"/><circle cx="5" cy="5" r="1.8" fill="#f5776a"/></svg></i><span>123, Lorem ipsum dolor<br>consectetur adipiscing</span></div>
<h4 class="abs f-head" style="left:837px">SUBSCRIBE TO OUR NEWSLETTER</h4>
<p class="abs newsletter-text">Sign up today to get resources on how to attract and retain more customers!</p>
<div class="abs email-field">Email Address
  <div class="abs email-send"><svg width="16" height="16" viewBox="0 0 16 16"><path d="M1 8l14-6-5 13-2-5z" fill="#fff"/></svg></div>
</div>
<div class="abs social" style="left:838px"></div>
<div class="abs social on" style="left:877px"></div>
<div class="abs social" style="left:916px"></div>
<div class="abs social" style="left:955px"></div>
<div class="abs chat"><svg width="20" height="18" viewBox="0 0 20 18"><path d="M10 1C5 1 1 4.3 1 8.3c0 2 1 3.8 2.6 5.1L3 17l4-2a10 10 0 0 0 3 .6c5 0 9-3.3 9-7.3S15 1 10 1z" fill="#fff"/><circle cx="6.5" cy="8.3" r="1.1" fill="#3fc5c5"/><circle cx="10" cy="8.3" r="1.1" fill="#3fc5c5"/><circle cx="13.5" cy="8.3" r="1.1" fill="#3fc5c5"/></svg></div>
<div class="abs footer-rule"></div>
<p class="abs copyright">Copyright© 2022 ByteQuest | &nbsp;All Rights Reserved.</p>

</body>
</html>
```